Newsletter Template to be emailed to clients

I require a newsletter template that I can edit and frequently update and embed into an email and send to my clients. HTML & CSS

I am seeking it to be attention grabbing, engaging and make use of social media buttons for users to further engage with Bright Harbors. Our business provides free career services to young professionals. Visit http://brightharborsgroup.example/home/

Important for the content to be able to be interactive, so clients can click onto hyperlinks and be taken to our site. The font style and colours need to match our corporate colours. The Images need to be high resolution and clear. Please submit your designs using material from our site so we can see what it could potentially look like.

Please see a template in the attachment to replicate with Bright Harbors colours and images. Combine image 1 and 2 together to see the whole template.
Updates

Project Deadline Extended Reason: I am not that impressed with the designs submitted. I would like more options. Added Monday, June 15, 2015

Hi All, Please note I have extended the deadline on this project because I am wanting more designs. Looking for something creative and catchy. Less font…only the most important things like heading, content etc Would like to see a section for career tools. Many thanks, Megan

Target Market(s)

20-30 year olds

Industry/Entity Type

Seeking

Font styles to use
Sans Serif

Requirements
Must have
• Bright Harbors logo - attached.
• Corporate Colours with font.
• Highlighted Career Tools separate from Blogs.
• Grey R66 G73 B74
• White R242 G240 B230
• Teal R38 G128 B138
• Clean white backdrop.
Nice to have
• Something modern and professional but trendy so it catches the attention of 20-30 year olds.

```html
<!DOCTYPE html>
<html lang="en">
<head>
<meta charset="UTF-8">
<title>Bright Harbors Newsletter</title>
<link href="https://fonts.googleapis.com/css2?family=Montserrat:wght@600;700;800&family=Open+Sans:wght@400;600&display=swap" rel="stylesheet">
<style>
  :root {
    --teal: #26808A;
    --teal-dark: #1f6c75;
    --grey: #42494A;
    --grey-soft: #9a9fa0;
    --button: #c9cccc;
    --paper: #F2F0E6;
    --white: #ffffff;
  }
  * { box-sizing: border-box; margin: 0; padding: 0; }
  html, body { width: 783px; height: 1200px; overflow: hidden; background: var(--white); }
  body { position: relative; font-family: 'Open Sans', sans-serif; color: var(--grey); }

  .masthead {
    position: absolute; left: 31px; top: 26px; width: 731px; height: 60px;
    display: flex; align-items: center; justify-content: space-between;
  }
  .brand { display: flex; align-items: center; gap: 12px; text-decoration: none; }
  .brand-dot { width: 30px; height: 30px; border-radius: 50%; background: var(--teal); }
  .brand-name {
    font-family: 'Montserrat', sans-serif; font-weight: 800; font-size: 24px;
    letter-spacing: 1px; color: var(--teal); text-transform: uppercase;
  }
  .social { display: flex; gap: 14px; list-style: none; }
  .social a {
    display: flex; align-items: center; justify-content: center;
    width: 52px; height: 52px; border-radius: 50%; background: var(--button);
    color: var(--white); text-decoration: none;
    font-family: 'Montserrat', sans-serif; font-weight: 700; font-size: 10px;
    letter-spacing: 0.5px; text-transform: uppercase;
  }

  .hero {
    position: absolute; left: 31px; top: 105px; width: 731px; height: 278px;
    background: linear-gradient(160deg, #7fd0d8 0%, #4fb2bd 45%, #2e8f99 100%);
  }
  .hero-tag {
    position: absolute; right: 12px; top: 12px; padding: 7px 14px;
    background: var(--teal); color: var(--white);
    font-family: 'Montserrat', sans-serif; font-weight: 700; font-size: 15px; letter-spacing: 1px;
  }

  .lead { position: absolute; left: 31px; top: 394px; width: 731px; text-align: center; }
  .lead-title {
    font-family: 'Montserrat', sans-serif; font-weight: 800; font-size: 44px;
    line-height: 48px; color: var(--teal); text-transform: uppercase; letter-spacing: 0.5px;
  }
  .lead-text { margin-top: 10px; padding: 0 14px; font-size: 14px; line-height: 19px; color: var(--grey); }

  .tools {
    position: absolute; left: 31px; top: 596px; width: 731px; height: 530px;
    background: var(--teal); border-top: 3px solid var(--teal-dark);
    padding: 0 12px 12px;
  }
  .tools-heading {
    height: 40px; display: flex; align-items: center; justify-content: center;
    margin: 0 -12px 12px; background: var(--paper); color: var(--teal);
    font-family: 'Montserrat', sans-serif; font-weight: 800; font-size: 16px;
    letter-spacing: 3px; text-transform: uppercase;
  }
  .tools-grid {
    display: grid; grid-template-columns: repeat(3, 1fr);
    grid-template-rows: 225px 225px; gap: 12px;
  }
  .tool { display: flex; flex-direction: column; text-decoration: none; }
  .tool-photo { height: 150px; }
  .tool-photo.is-person { background: linear-gradient(150deg, #f6d3dc, #e9a9bb); }
  .tool-photo.is-eggs { background: linear-gradient(150deg, #efe3d2, #d9c3a6); }
  .tool-photo.is-wallet { background: linear-gradient(150deg, #6b6660, #2f2b28); }
  .tool-caption {
    flex: 1; display: flex; align-items: center; justify-content: center; text-align: center;
    padding: 0 8px; color: var(--white);
    font-family: 'Montserrat', sans-serif; font-weight: 700; font-size: 16px; line-height: 20px;
    text-transform: uppercase;
  }

  .footer {
    position: absolute; left: 31px; top: 1138px; width: 731px; text-align: center;
    font-size: 10.5px; line-height: 14px; color: var(--grey-soft);
  }
</style>
</head>
<body>
  <header class="masthead">
    <a class="brand" href="http://brightharborsgroup.example/home/">
      <span class="brand-dot"></span>
      <span class="brand-name">Bright Harbors</span>
    </a>
    <ul class="social">
      <li><a href="#">Post</a></li>
      <li><a href="#">Like</a></li>
      <li><a href="#">Link</a></li>
      <li><a href="#">Snap</a></li>
    </ul>
  </header>

  <section class="hero" role="img" aria-label="Person in a light teal sweater with sunglasses hooked on the collar">
    <span class="hero-tag">NEWSROOM</span>
  </section>

  <section class="lead">
    <h1 class="lead-title">The Resume Mistakes<br>You'll Want to Fix ASAP</h1>
    <p class="lead-text">Let's say it takes you five minutes to read this article. In the same time span, a hiring manager will look at around 50 resumes. That certainly doesn't seem like enough time to absorb all your accomplishments, skills, experiences, and qualifications. And it's not! So it's critical that there aren't any errors on your resume—because</p>
  </section>

  <section class="tools" aria-labelledby="tools-heading">
    <h2 class="tools-heading" id="tools-heading">Career Tools</h2>
    <div class="tools-grid">
      <a class="tool" href="#">
        <div class="tool-photo is-person" role="img" aria-label="Young woman in pink holding a phone"></div>
        <div class="tool-caption">Welcome to Bright Harbors</div>
      </a>
      <a class="tool" href="#">
        <div class="tool-photo is-eggs" role="img" aria-label="Eggs in a carton, one with a drawn moustache"></div>
        <div class="tool-caption">Love the fact you're different</div>
      </a>
      <a class="tool" href="#">
        <div class="tool-photo is-wallet" role="img" aria-label="Hands taking cash from a wallet"></div>
        <div class="tool-caption">9 words to use with your banker</div>
      </a>
      <a class="tool" href="#">
        <div class="tool-photo is-person" role="img" aria-label="Young woman in pink holding a phone"></div>
        <div class="tool-caption">Welcome to Bright Harbors</div>
      </a>
      <a class="tool" href="#">
        <div class="tool-photo is-eggs" role="img" aria-label="Eggs in a carton, one with a drawn moustache"></div>
        <div class="tool-caption">Love the fact you're different</div>
      </a>
      <a class="tool" href="#">
        <div class="tool-photo is-wallet" role="img" aria-label="Hands taking cash from a wallet"></div>
        <div class="tool-caption">9 words to use with your banker</div>
      </a>
    </div>
  </section>

  <footer class="footer">
    <p>2015 Bright Harbors. All Rights Reserved.</p>
    <p>Bright Harbors, Bright Harbors logo, Bright Harbors Custom Stamps, Bright Harbors Profile Cards</p>
    <p>are registered trademarks or trademarks of Bright Harbors.</p>
  </footer>
</body>
</html>
```